Teach English in China Website Redesign Needed

We recruit native English speakers from the US, UK, etc. who want to teach English as a foreign language in schools in China. Our target customer is college educated, age 22-28 and they love to travel. We prefer designs with bright colors and lots of photos. We want to keep all the text on our current homepage, BrightPathTutors.com. We are open to changing our logo. A competitor's page that we like is bluekitemeadow.com because of their bright colors, photos and use of white space. We are happy to give you a dofollow link and design credit on our homepage. The use of included photos is optional. We need at least a home page design and a standard blog post design.
Target Market(s)
Our target customer is college educated, age 22-28 and they love to travel. Half of our customers are kindergarten teachers. Half of our customers are male.
Logo Text
Bright Path Tutors
Number of Pages Required
Requirements
Must have
- Bright colors
Should not have
- Our homepage must not look crowded. Use white space effectively.

```html
<!DOCTYPE html>
<html lang="en">
<head>
<meta charset="utf-8">
<title>Bright Path Tutors – Teaching Jobs in China</title>
<link href="https://fonts.googleapis.com/css2?family=Signika:wght@400;600&family=Open+Sans:ital,wght@0,400;0,600;0,700;1,400&display=swap" rel="stylesheet">
<style>
:root{
  --red:#e2231a;
  --yellow:#ffd500;
  --ink:#222;
  --text:#555;
  --muted:#888;
  --card:#ececec;
  --dark:#1f1f1f;
  --navy:#171c2b;
  --white:#fff;
}
*{box-sizing:border-box;margin:0;padding:0}
html,body{width:1200px;height:4787px;overflow:hidden}
body{font-family:"Open Sans",Arial,sans-serif;color:var(--text);background:var(--white);font-size:14px;line-height:1.6}
h1,h2,h3,h4{font-family:"Signika",Arial,sans-serif;font-weight:600;color:var(--ink)}
.wrap{width:970px;margin:0 auto;position:relative}
.btn{display:inline-block;background:var(--yellow);color:var(--ink);font-weight:600;font-size:15px;padding:9px 38px;border-radius:4px;text-decoration:none}
.section-title{text-align:center;font-size:40px;font-weight:400}
.section-title span{color:var(--red)}

/* top bar */
.topbar{height:32px;background:var(--dark);color:#ccc;font-size:12px}
.topbar .wrap{display:flex;justify-content:space-between;align-items:center;height:32px}
.topbar .contact{display:flex;gap:28px}
.topbar .contact span{display:flex;align-items:center;gap:7px}
.social{display:flex;gap:6px}
.social i{width:22px;height:22px;border-radius:50%;background:#555;display:block}

/* header */
.header{height:112px}
.header .wrap{display:flex;justify-content:space-between;align-items:stretch;height:112px}
.brand{display:flex;align-items:center;gap:12px}
.brand-dot{width:46px;height:46px;border-radius:50%;background:var(--red)}
.brand-name{font-family:"Signika",sans-serif;font-weight:600;font-size:30px;color:var(--red);line-height:1}
.nav{display:flex;align-items:stretch;list-style:none}
.nav li{display:flex;align-items:center;padding:0 18px;font-family:"Signika",sans-serif;font-size:18px;color:var(--ink)}
.nav li.active{background:var(--yellow)}

/* hero */
.hero{height:551px;position:relative;background:linear-gradient(180deg,#6f9fd0 0%,#a9c6e2 38%,#8a97a6 70%,#3b4a5c 100%)}
.hero-text{position:absolute;left:118px;top:120px}
.hero-text .kicker{font-family:"Signika",sans-serif;font-weight:600;font-size:40px;color:var(--white);letter-spacing:1px}
.hero-text .big{font-family:"Signika",sans-serif;font-weight:600;font-size:96px;color:var(--red);letter-spacing:14px;line-height:1}
.hero-text .btn{margin-top:34px;padding:12px 60px}
.dots{position:absolute;bottom:14px;left:50%;transform:translateX(-50%);display:flex;gap:8px}
.dots i{width:10px;height:10px;border-radius:50%;background:rgba(255,255,255,.6);display:block}
.dots i.on{background:var(--red)}

/* about */
.about{height:545px;padding-top:70px}
.about .section-title{margin-bottom:40px}
.about-row{display:flex;justify-content:space-between}
.about-copy{width:470px}
.about-copy h3{font-size:26px;font-weight:400;margin-bottom:14px}
.about-copy p{font-size:13px;color:var(--muted);line-height:1.75;margin-bottom:20px}
.about-photo{width:453px;height:300px;background:linear-gradient(135deg,#c9b8a2,#9a3b32 55%,#e9e2d8)}

/* how it works */
.how{height:537px;padding-top:100px;text-align:center}
.steps{display:flex;justify-content:space-between;margin:56px 0 28px}
.step{width:210px}
.step svg{width:66px;height:66px;margin-bottom:12px}
.step h4{font-size:24px;font-weight:400;margin-bottom:8px}
.step p{font-size:13px;color:var(--ink);line-height:1.5}

/* highlights */
.highlights{height:472px;display:flex}
.highlights-photo{width:606px;background:linear-gradient(160deg,#152a4a 0%,#2b3f2e 55%,#b5482a 80%,#1a2a3c 100%)}
.highlights-panel{flex:1;background:var(--navy);padding:40px 30px 0 28px;color:#ddd}
.highlights-panel h3{color:var(--white);font-size:28px;font-weight:400;margin-bottom:14px}
.highlights-panel ul{list-style:none}
.highlights-panel li{display:flex;gap:10px;font-size:13px;line-height:1.45;margin-bottom:7px}
.highlights-panel li svg{flex:0 0 14px;height:14px;margin-top:2px}

/* testimonials */
.testimonials{height:558px;padding-top:70px}
.testimonials .section-title{margin-bottom:36px}
.reviews{display:flex;justify-content:space-between;width:820px;margin:0 auto}
.review{width:252px;text-align:center}
.review-card{background:var(--card);padding:70px 24px 26px;position:relative;margin-top:60px}
.avatar{position:absolute;top:-60px;left:50%;transform:translateX(-50%);width:118px;height:118px;border-radius:50%;border:5px solid var(--white);background:linear-gradient(135deg,#d8c2a8,#7b5b45)}
.review-card p{font-style:italic;font-size:14px;color:var(--muted);line-height:1.6}
.review h4{color:var(--red);font-size:21px;font-weight:400;margin-top:20px}
.review .role{font-size:14px;color:var(--ink)}
.arrow{position:absolute;top:230px;width:40px;height:40px;border-radius:50%;background:var(--yellow);display:flex;align-items:center;justify-content:center}
.arrow.left{left:0}.arrow.right{right:0}

/* apply */
.apply{height:453px;background:linear-gradient(90deg,#3a3a3a,#5b5b5b 50%,#3a3a3a);display:flex;flex-direction:column;align-items:center;justify-content:center;text-align:center}
.apply h2{color:var(--white);font-size:56px;font-weight:400}
.apply p{color:var(--white);font-size:18px;margin:8px 0 22px}

/* blog */
.blog{height:1110px;padding-top:110px;text-align:center}
.blog .section-title{margin-bottom:60px}
.posts{display:grid;grid-template-columns:repeat(3,313px);gap:50px 15px;text-align:left}
.post-img{height:185px}
.post-body{background:var(--card);padding:14px 18px 14px;height:165px}
.post-body h4{font-size:16px;font-weight:400;margin-bottom:6px}
.post-body p{font-size:13px;color:var(--text);line-height:1.5}
.post-body p a{color:var(--red);text-decoration:none}
.post-meta{font-size:13px;color:var(--ink);margin-top:8px}
.post-meta b{color:var(--red);font-weight:400}
.blog .btn{margin-top:70px;padding:10px 60px}

/* footer */
.footer{height:417px;background:var(--dark);color:#bbb;position:relative}
.footer .wrap{display:flex;padding-top:78px}
.footer h4{color:var(--white);font-size:26px;font-weight:400;margin-bottom:20px}
.foot-brand{width:330px}
.foot-brand .brand-name{color:var(--white);font-size:26px}
.foot-brand p{font-size:14px;color:#ccc;margin-top:26px;line-height:1.75;width:270px}
.foot-address{width:260px}
.foot-address li{display:flex;gap:12px;font-size:12px;margin-bottom:14px;align-items:center}
.foot-address li i{width:26px;height:26px;border:1px solid #555;display:block;flex:0 0 26px}
.foot-nav{width:220px}
.foot-nav li{display:flex;gap:10px;align-items:center;font-size:13px;margin-bottom:10px}
.footer ul{list-style:none}
.foot-social .squares{display:flex;gap:6px}
.foot-social .squares i{width:26px;height:26px;border:1px solid #777;display:block}
.copyright{position:absolute;bottom:0;left:0;right:0;border-top:1px solid #333;height:48px;line-height:48px;text-align:center;font-size:12px;color:#888}
.live-chat{position:absolute;right:25px;bottom:0;width:210px;height:40px;background:var(--red);color:var(--white);font-weight:700;font-size:14px;display:flex;align-items:center;justify-content:center;gap:10px;border-radius:4px 4px 0 0}
</style>
</head>
<body>

<div class="topbar">
  <div class="wrap">
    <div class="contact">
      <span><svg width="12" height="12" viewBox="0 0 24 24"><path fill="#ccc" d="M6.6 10.8a15 15 0 006.6 6.6l2.2-2.2a1 1 0 011-.25 11 11 0 003.6.6 1 1 0 011 1V20a1 1 0 01-1 1A17 17 0 013 4a1 1 0 011-1h3.5a1 1 0 011 1 11 11 0 00.6 3.6 1 1 0 01-.25 1z"/></svg>555-010-2468</span>
      <span><svg width="13" height="11" viewBox="0 0 24 18"><rect x="1" y="1" width="22" height="16" fill="none" stroke="#ccc" stroke-width="2"/><path d="M1 1l11 9 11-9" fill="none" stroke="#ccc" stroke-width="2"/></svg>hello@brightpathtutors.com</span>
    </div>
    <div class="social"><i></i><i></i><i></i><i></i></div>
  </div>
</div>

<header class="header">
  <div class="wrap">
    <div class="brand"><span class="brand-dot"></span><span class="brand-name">Bright Path Tutors</span></div>
    <ul class="nav">
      <li class="active">Home</li><li>Available Jobs</li><li>Apply Online</li><li>Blog</li><li>FAQ</li>
    </ul>
  </div>
</header>

<section class="hero" role="img" aria-label="City skyline with a tall broadcast tower beside the river under a blue sky">
  <div class="hero-text">
    <div class="kicker">TEACHING JOBS IN</div>
    <div class="big">CHINA</div>
    <a class="btn" href="#">Apply Now</a>
  </div>
  <div class="dots"><i></i><i class="on"></i><i></i></div>
</section>

<section class="about">
  <div class="wrap">
    <h2 class="section-title">Teach English in <span>China</span></h2>
    <div class="about-row">
      <div class="about-copy">
        <h3>About Us</h3>
        <p>Want to teach English in China? Do you love teaching children or adults? Would you like the adventure of teaching in China for a year? Then we have the perfect job for you! We are seeking English speakers from the US, UK, Canada, Ireland, Australia, New Zealand and South Africa to teach English in China for a year (or longer if you wish). We recruit for hundreds of schools all over China such as Northstar English, Harbor Lane English, Silkroute Learning, Cedar Hill English, Skyarch Academy, Keystone Kids, Amber Orchard, public schools, international schools, universities, and more.</p>
        <a class="btn" href="#">Read More</a>
      </div>
      <div class="about-photo" role="img" aria-label="Classroom of young pupils in red uniforms seated at desks"></div>
    </div>
  </div>
</section>

<section class="how">
  <div class="wrap">
    <h2 class="section-title">How it <span>Works</span></h2>
    <div class="steps">
      <div class="step">
        <svg viewBox="0 0 64 64"><rect x="14" y="10" width="36" height="46" rx="3" fill="none" stroke="#e2231a" stroke-width="4"/><rect x="24" y="6" width="16" height="8" rx="2" fill="#e2231a"/><path d="M21 26h22M21 34h22M21 42h14" stroke="#e2231a" stroke-width="3"/></svg>
        <h4>Apply</h4>
        <p>Lorem Ipsum has been the industry's standard dummy text ever since the 1500s.</p>
      </div>
      <div class="step">
        <svg viewBox="0 0 64 64"><path d="M32 10c15 0 26 8 26 19s-11 19-26 19c-3 0-6 0-8-1l-12 8 3-11C9 40 6 35 6 29 6 18 17 10 32 10z" fill="none" stroke="#e2231a" stroke-width="4"/><path d="M20 25h24M20 33h18" stroke="#e2231a" stroke-width="3"/></svg>
        <h4>Interview</h4>
        <p>Lorem Ipsum has been the industry's standard dummy text ever since the 1500s.</p>
      </div>
      <div class="step">
        <svg viewBox="0 0 64 64"><rect x="8" y="12" width="48" height="44" rx="3" fill="none" stroke="#e2231a" stroke-width="4"/><rect x="8" y="12" width="48" height="10" fill="#e2231a"/><path d="M20 6v12M44 6v12" stroke="#e2231a" stroke-width="4"/><g fill="#e2231a"><rect x="15" y="28" width="8" height="7"/><rect x="28" y="28" width="8" height="7"/><rect x="41" y="28" width="8" height="7"/><rect x="15" y="41" width="8" height="7"/><rect x="28" y="41" width="8" height="7"/><rect x="41" y="41" width="8" height="7"/></g></svg>
        <h4>Start Work</h4>
        <p>Lorem Ipsum has been the industry's standard dummy text ever since the 1500s.</p>
      </div>
      <div class="step">
        <svg viewBox="0 0 64 64"><path d="M32 56L9 33C2 26 4 13 14 11c7-1 13 3 18 10 5-7 11-11 18-10 10 2 12 15 5 22z" fill="#e2231a"/></svg>
        <h4>Free Service</h4>
        <p>Lorem Ipsum has been the industry's standard dummy text ever since the 1500s.</p>
      </div>
    </div>
    <a class="btn" href="#">Apply Now</a>
  </div>
</section>

<section class="highlights">
  <div class="highlights-photo" role="img" aria-label="Illuminated red pagoda among trees at dusk"></div>
  <div class="highlights-panel">
    <h3>Highlights</h3>
    <ul>
      <li><svg viewBox="0 0 14 14"><path d="M2 7l3 3 7-7" fill="none" stroke="#e2231a" stroke-width="2.4"/></svg>Competitive compensation 7000-9000 RMB/month, up to 18,000 RMB (divide by 6.5 for US dollars) if you have a bachelor's degree</li>
      <li><svg viewBox="0 0 14 14"><path d="M2 7l3 3 7-7" fill="none" stroke="#e2231a" stroke-width="2.4"/></svg>2+ years of teaching experience</li>
      <li><svg viewBox="0 0 14 14"><path d="M2 7l3 3 7-7" fill="none" stroke="#e2231a" stroke-width="2.4"/></svg>Housing allowance: 2000 RMB/month (housing is cheaper in China)</li>
      <li><svg viewBox="0 0 14 14"><path d="M2 7l3 3 7-7" fill="none" stroke="#e2231a" stroke-width="2.4"/></svg>Teach private English lessons after work (ex 250 RMB/hr, $38 US per hour)</li>
      <li><svg viewBox="0 0 14 14"><path d="M2 7l3 3 7-7" fill="none" stroke="#e2231a" stroke-width="2.4"/></svg>Airfare reimbursement: 5000 RMB at end of completed 1 year contract</li>
      <li><svg viewBox="0 0 14 14"><path d="M2 7l3 3 7-7" fill="none" stroke="#e2231a" stroke-width="2.4"/></svg>Free TESOL / TEFL training and certificate</li>
      <li><svg viewBox="0 0 14 14"><path d="M2 7l3 3 7-7" fill="none" stroke="#e2231a" stroke-width="2.4"/></svg>Invitation letter so you can apply for a visa Z (if you have a bachelor's degree)</li>
      <li><svg viewBox="0 0 14 14"><path d="M2 7l3 3 7-7" fill="none" stroke="#e2231a" stroke-width="2.4"/></svg>Airport pickup</li>
      <li><svg viewBox="0 0 14 14"><path d="M2 7l3 3 7-7" fill="none" stroke="#e2231a" stroke-width="2.4"/></svg>5-day work week, 25 hours teaching per week plus some office hours</li>
      <li><svg viewBox="0 0 14 14"><path d="M2 7l3 3 7-7" fill="none" stroke="#e2231a" stroke-width="2.4"/></svg>10 paid holidays</li>
      <li><svg viewBox="0 0 14 14"><path d="M2 7l3 3 7-7" fill="none" stroke="#e2231a" stroke-width="2.4"/></svg>Free Chinese classes 2 hours per week with most jobs</li>
    </ul>
  </div>
</section>

<section class="testimonials">
  <div class="wrap">
    <h2 class="section-title">Teachers Says <span>About Us</span></h2>
    <span class="arrow left"><svg width="14" height="14" viewBox="0 0 14 14"><path d="M9 2L4 7l5 5" fill="none" stroke="#222" stroke-width="2.4"/></svg></span>
    <span class="arrow right"><svg width="14" height="14" viewBox="0 0 14 14"><path d="M5 2l5 5-5 5" fill="none" stroke="#222" stroke-width="2.4"/></svg></span>
    <div class="reviews">
      <div class="review">
        <div class="review-card"><span class="avatar" role="img" aria-label="Portrait photo of a teacher"></span><p>"When I began the search for a teaching job in China, I had no idea what to expect. Luckily I came across Maya with BrightPathTutors.com."</p></div>
        <h4>Lorem Ipsum</h4><div class="role">Teacher</div>
      </div>
      <div class="review">
        <div class="review-card"><span class="avatar" role="img" aria-label="Portrait photo of a teacher"></span><p>"When I began my search for a teaching job in China, I had no idea what to expect. Luckily I came across Maya with BrightPathTutors.com."</p></div>
        <h4>Lorem Ipsum</h4><div class="role">Teacher</div>
      </div>
      <div class="review">
        <div class="review-card"><span class="avatar" role="img" aria-label="Portrait photo of a teacher"></span><p>"When I began my search for a teaching job in China, I had no idea what to expect. Luckily I came across Maya with BrightPathTutors.com."</p></div>
        <h4>Lorem Ipsum</h4><div class="role">Teacher</div>
      </div>
    </div>
  </div>
</section>

<section class="apply" role="img" aria-label="Group of smiling young adults studying together at a table">
  <h2>Apply For Job</h2>
  <p>Hundreds of teaching jobs in China, fully screened, updated daily.</p>
  <a class="btn" href="#">Apply Now</a>
</section>

<section class="blog">
  <div class="wrap">
    <h2 class="section-title">Recent <span>Blog Post</span></h2>
    <div class="posts">
      <article><div class="post-img" role="img" aria-label="Children playing with colourful toys in a classroom" style="background:linear-gradient(135deg,#c0392b,#e0a95a 60%,#7a4a2a)"></div><div class="post-body"><h4>Lorem Ipsum Dolar Smit</h4><p>Lorem Ipsum has been the industry's standard dummy text ever since the 1500s. <a href="#">Read More</a></p><div class="post-meta">By <b>Admin</b> - Apr 5, 2017</div></div></article>
      <article><div class="post-img" role="img" aria-label="Young boy at a desk with a globe and books" style="background:linear-gradient(135deg,#d9e4ec,#c44a3a 55%,#f0e6d8)"></div><div class="post-body"><h4>Lorem Ipsum Dolar Smit</h4><p>Lorem Ipsum has been the industry's standard dummy text ever since the 1500s. <a href="#">Read More</a></p><div class="post-meta">By <b>Admin</b> - Apr 5, 2017</div></div></article>
      <article><div class="post-img" role="img" aria-label="Children playing football on a green field" style="background:linear-gradient(180deg,#8fb3d6,#3f8a3a 55%,#2f6f2a)"></div><div class="post-body"><h4>Lorem Ipsum Dolar Smit</h4><p>Lorem Ipsum has been the industry's standard dummy text ever since the 1500s. <a href="#">Read More</a></p><div class="post-meta">By <b>Admin</b> - Apr 5, 2017</div></div></article>
      <article><div class="post-img" role="img" aria-label="Large classroom of students seated in rows" style="background:linear-gradient(135deg,#6b6f78,#b7a98f 55%,#3a3d44)"></div><div class="post-body"><h4>Lorem Ipsum Dolar Smit</h4><p>Lorem Ipsum has been the industry's standard dummy text ever since the 1500s. <a href="#">Read More</a></p><div class="post-meta">By <b>Admin</b> - Apr 5, 2017</div></div></article>
      <article><div class="post-img" role="img" aria-label="Young pupils in red uniforms at their desks" style="background:linear-gradient(135deg,#e8dcc8,#c0392b 55%,#6b3a2a)"></div><div class="post-body"><h4>Lorem Ipsum Dolar Smit</h4><p>Lorem Ipsum has been the industry's standard dummy text ever since the 1500s. <a href="#">Read More</a></p><div class="post-meta">By <b>Admin</b> - Apr 5, 2017</div></div></article>
      <article><div class="post-img" role="img" aria-label="Teacher with a group of students in a classroom" style="background:linear-gradient(135deg,#4a3a32,#a0643c 55%,#d8c4a4)"></div><div class="post-body"><h4>Lorem Ipsum Dolar Smit</h4><p>Lorem Ipsum has been the industry's standard dummy text ever since the 1500s. <a href="#">Read More</a></p><div class="post-meta">By <b>Admin</b> - Apr 5, 2017</div></div></article>
    </div>
    <a class="btn" href="#">Load More</a>
  </div>
</section>

<footer class="footer">
  <div class="wrap">
    <div class="foot-brand">
      <div class="brand"><span class="brand-dot"></span><span class="brand-name">Bright Path Tutors</span></div>
      <p>Lorem Ipsum has been the industry's standard dummy text ever since the 1500s. Lorem Ipsum has been the industry's standard dummy text ever since the 1500s.</p>
    </div>
    <div class="foot-address">
      <h4>Address</h4>
      <ul>
        <li><i></i>48 Maple Row, Suite 12,<br>Springfield 00000</li>
        <li><i></i>555-010-7731</li>
        <li><i></i>hello@brightpathtutors.com</li>
      </ul>
    </div>
    <div class="foot-nav">
      <h4>Navigation</h4>
      <ul>
        <li><svg width="10" height="10" viewBox="0 0 10 10"><path d="M2 1l5 4-5 4" fill="none" stroke="#ffd500" stroke-width="2"/></svg>Home</li>
        <li><svg width="10" height="10" viewBox="0 0 10 10"><path d="M2 1l5 4-5 4" fill="none" stroke="#ffd500" stroke-width="2"/></svg>Available Jobs</li>
        <li><svg width="10" height="10" viewBox="0 0 10 10"><path d="M2 1l5 4-5 4" fill="none" stroke="#ffd500" stroke-width="2"/></svg>Apply Online</li>
        <li><svg width="10" height="10" viewBox="0 0 10 10"><path d="M2 1l5 4-5 4" fill="none" stroke="#ffd500" stroke-width="2"/></svg>Blog</li>
        <li><svg width="10" height="10" viewBox="0 0 10 10"><path d="M2 1l5 4-5 4" fill="none" stroke="#ffd500" stroke-width="2"/></svg>FAQ</li>
      </ul>
    </div>
    <div class="foot-social">
      <h4>Social Media</h4>
      <div class="squares"><i></i><i></i><i></i><i></i></div>
    </div>
  </div>
  <div class="copyright">© 2017, All rights reserved</div>
  <div class="live-chat"><svg width="18" height="16" viewBox="0 0 24 20"><path d="M12 1c6 0 11 3.6 11 8s-5 8-11 8c-1.5 0-3-.2-4-.6L3 19l1.5-4C2.3 13.5 1 11.4 1 9c0-4.4 5-8 11-8z" fill="#fff"/></svg>LIVE CHAT</div>
</footer>

</body>
</html>
```